New Website for Manufacturing Company - PSD only, no coding - CLOSED TO NEW DESIGNERS

IF YOU HAVE NOT ALREADY SUBMITTED A DESIGN PLEASE DO NOT SUBMIT ONE.
This is a re-work of an existing website. We can keep the themes and color schemes the same but we will be changing the layout and page content.
The scope includes the creation of some icons/sketches that will form some of the page content.
The scope is design only, no coding.
There are four files that have been uploaded that give a more detailed project brief, please read them.
Target Market(s)
Manufacturing
Industry/Entity Type
It Company
Number of Pages Required
1 page
Look and feel
Each slider illustrates characteristics of the customer's brand and the style your logo design should communicate.

```html
<!DOCTYPE html>
<html lang="en">
<head>
<meta charset="utf-8">
<title>Corvane Manufacturing</title>
<link href="https://fonts.googleapis.com/css2?family=Open+Sans:wght@400;600;700&display=swap" rel="stylesheet">
<style>
:root{
  --blue:#1f6fc1;
  --blue-dark:#14508f;
  --navy:#0f2740;
  --navy-deep:#0a1b2d;
  --ink:#333;
  --muted:#777;
  --line:#dcdcdc;
  --paper:#f3f4f6;
  --white:#fff;
}
*{box-sizing:border-box;margin:0;padding:0}
html,body{width:1200px;height:2284px;overflow:hidden}
body{font-family:"Open Sans",Arial,sans-serif;color:var(--ink);background:var(--white);font-size:12px;position:relative}
.wrap{width:900px;margin:0 auto;position:relative}
/* header */
.topbar{height:78px;position:relative}
.brand{position:absolute;left:160px;top:6px;background:var(--blue);color:var(--white);font-weight:700;font-size:26px;padding:8px 16px;letter-spacing:1px}
.contact-top{position:absolute;right:150px;top:8px;text-align:right}
.contact-top .tag{display:inline-block;background:var(--blue);color:#fff;font-size:10px;padding:2px 10px;margin-bottom:4px}
.contact-top .phone{font-size:22px;font-weight:700;color:var(--blue-dark)}
.contact-top .mail{font-size:12px;color:var(--blue-dark)}
.nav{height:30px;background:var(--blue-dark);margin-top:10px}
.nav .wrap{display:flex;align-items:center;height:30px}
.nav a{color:#fff;font-size:11px;text-decoration:none;padding:0 14px;line-height:30px}
.nav a.active{background:var(--blue)}
.nav .quote{margin-left:auto;background:#e8f1fb;color:var(--blue-dark);line-height:20px;padding:0 10px;font-weight:600}
.nav .chat{display:flex;align-items:center;gap:5px}
/* hero */
.hero{height:340px;background:linear-gradient(180deg,#3384d4,#1d66b4);position:relative;color:#fff}
.hero-art{position:absolute;left:0;top:0;width:540px;height:340px;background:linear-gradient(120deg,rgba(255,255,255,.18),rgba(255,255,255,0))}
.hero-copy{position:absolute;left:552px;top:78px;width:580px}
.hero-copy h1{font-weight:400;font-size:28px;line-height:36px}
.hero-copy .pill{display:inline-block;background:#fff;color:var(--blue-dark);font-size:20px;padding:3px 14px;margin-top:8px}
.hero-copy .btn{display:inline-block;background:var(--navy);color:#fff;font-size:12px;padding:6px 14px;margin:16px 0 0 190px}
.arrow{position:absolute;top:152px}
/* about */
.about{height:340px;background:var(--paper);position:relative}
.about-art{position:absolute;right:0;top:0;width:640px;height:340px;background:linear-gradient(90deg,rgba(243,244,246,1),rgba(205,212,222,.7))}
.about .wrap{padding-top:26px}
.about h2{font-size:15px;font-weight:700;margin-bottom:8px}
.about p{width:380px;font-size:11px;line-height:17px;color:#555}
.about h3{font-size:13px;font-weight:700;margin:14px 0 6px}
.about li{list-style:none;font-size:11px;color:#445;display:flex;align-items:center;gap:8px;line-height:26px}
.section-title{font-size:16px;font-weight:600;color:var(--ink);padding:22px 0 12px;border-bottom:1px solid var(--line);margin-bottom:16px}
.section-title small{font-size:10px;color:#999;font-weight:400}
/* capabilities */
.capabilities{height:610px}
.grid{display:grid;grid-template-columns:repeat(4,210px);column-gap:20px;row-gap:22px}
.card{border:1px solid var(--line);height:232px;padding:0 0 10px;background:#fff}
.card .art{height:108px;background:linear-gradient(180deg,#fafafa,#e6e8eb)}
.card h4{font-size:13px;font-weight:600;text-align:center;padding:6px 0 2px}
.card p{font-size:10px;line-height:14px;color:var(--muted);padding:0 14px}
.card .more{display:block;width:70px;margin:8px auto 0;background:var(--blue);color:#fff;font-size:9px;text-align:center;line-height:18px}
.form{border:1px solid var(--line);height:232px}
.form h4{background:var(--blue);color:#fff;font-size:13px;font-weight:600;text-align:center;line-height:30px}
.form .field{margin:10px 12px 0;height:20px;border:1px solid var(--line);font-size:9px;color:#999;padding:3px 6px}
.form .field.big{height:40px}
.form .send{float:right;margin:10px 12px 0;background:var(--blue);color:#fff;font-size:9px;padding:3px 12px}
/* products */
.products{height:300px;background:#fafafa}
.products .pcards{display:grid;grid-template-columns:repeat(4,210px);column-gap:20px}
.pcard{border:1px solid var(--line);background:#fff;height:198px}
.pcard .art{height:118px;margin:6px;background:linear-gradient(180deg,#f5f5f5,#dfe2e6)}
.pcard h4{font-size:11px;font-weight:600;padding:2px 10px}
.pcard p{font-size:9px;line-height:12px;color:var(--muted);padding:2px 10px}
/* band */
.band{height:44px;background:var(--blue);color:#fff;text-align:center;font-size:13px;line-height:44px}
.band u{color:#cfe4ff}
/* footer */
.footer{height:486px;background:var(--navy);color:#c7d3e0}
.cols{display:grid;grid-template-columns:repeat(6,1fr);padding-top:30px}
.cols h5{color:#fff;font-size:11px;font-weight:700;margin-bottom:10px}
.cols li{list-style:none;font-size:10px;line-height:17px}
.fmeta{display:flex;gap:40px;margin-top:40px;border-top:1px solid #24405e;padding-top:24px}
.fmeta .item{display:flex;gap:8px;font-size:10px;line-height:17px}
.map{margin-left:auto;width:240px;height:150px;background:linear-gradient(135deg,#e8ecef,#cfd8df)}
.bottom{height:36px;background:var(--navy-deep);color:#8fa3b8;font-size:10px}
.bottom .wrap{display:flex;justify-content:space-between;line-height:36px}
</style>
</head>
<body>
<header>
  <div class="topbar">
    <div class="brand">CORVANE</div>
    <div class="contact-top">
      <span class="tag">International / Contact</span>
      <div class="phone">&#9742; 555.014.2200</div>
      <div class="mail">contact@corvanemfg.com</div>
    </div>
  </div>
  <nav class="nav"><div class="wrap">
    <a class="active">HOME</a><a>MAB</a><a>INDUSTRIAL</a><a>CUSTOM MANUFACTURING</a><a>ABOUT US</a><a>CONTACT US</a>
    <a class="quote">Request for Quote</a>
    <a class="chat"><svg width="12" height="10"><rect width="12" height="8" rx="2" fill="#fff"/></svg>Live Chat</a>
  </div></nav>
</header>

<section class="hero">
  <div class="hero-art" role="img" aria-label="Line illustration of insulation chambers and industrial equipment"></div>
  <svg class="arrow" style="left:30px" width="20" height="36"><path d="M16 2 L4 18 L16 34" stroke="#fff" stroke-width="3" fill="none"/></svg>
  <svg class="arrow" style="right:30px" width="20" height="36"><path d="M4 2 L16 18 L4 34" stroke="#fff" stroke-width="3" fill="none"/></svg>
  <div class="hero-copy">
    <h1>Manufacturer, Fabricator and distributor of high temperature insulating materials</h1>
    <span class="pill">High temperature insulation experts</span><br>
    <span class="btn">Detail</span>
  </div>
</section>

<section class="about">
  <div class="about-art" role="img" aria-label="Faint technical sketch of a manufacturing machine"></div>
  <div class="wrap">
    <h2>About Corvane Chambers</h2>
    <p>New England's largest distributor of thermal ceramics and kiln products. We stock a wide range of high temperature insulating material in our 60,000 sqft warehouses and are equipped to fulfil customer needs quickly and efficiently.</p>
    <h3>What we do</h3>
    <ul>
      <li><svg width="10" height="10"><circle cx="5" cy="5" r="5" fill="#e0762b"/></svg>Stocking Distributor of Refractory Products &#9679;</li>
      <li><svg width="10" height="10"><circle cx="5" cy="5" r="5" fill="#1f6fc1"/></svg>Manufacturing &ndash; Combustion Chamber Kits &#9679;</li>
      <li><svg width="10" height="10"><circle cx="5" cy="5" r="5" fill="#1f6fc1"/></svg>Manufacturing &ndash; Custom Vacuum Forming and Cast Shapes &#9679;</li>
      <li><svg width="10" height="10"><circle cx="5" cy="5" r="5" fill="#1f6fc1"/></svg>Fabrication &ndash; Die Cutting, Assembly, Fabrication &amp; Mixing &#9679;</li>
    </ul>
  </div>
</section>

<section class="capabilities"><div class="wrap">
  <div class="section-title">Our Capabilities</div>
  <div class="grid">
    <div class="card"><div class="art" role="img" aria-label="Sketch of a waterjet cutting machine"></div><h4>Waterjet Cutting</h4><p>Lorem ipsum dolor sit amet, consectetur adipiscing elit, sed do eiusmod tempor incididunt.</p><span class="more">VIEW MORE</span></div>
    <div class="card"><div class="art" role="img" aria-label="Sketch of casting equipment"></div><h4>Casting</h4><p>Lorem ipsum dolor sit amet, consectetur adipiscing elit, sed do eiusmod tempor incididunt.</p><span class="more">VIEW MORE</span></div>
    <div class="card"><div class="art" role="img" aria-label="Sketch of a laminating press"></div><h4>Laminating</h4><p>Lorem ipsum dolor sit amet, consectetur adipiscing elit, sed do eiusmod tempor incididunt.</p><span class="more">VIEW MORE</span></div>
    <div class="card"><div class="art" role="img" aria-label="Sketch of a CNC machine"></div><h4>CNC Machining</h4><p>Lorem ipsum dolor sit amet, consectetur adipiscing elit, sed do eiusmod tempor incididunt.</p><span class="more">VIEW MORE</span></div>
    <div class="card"><div class="art" role="img" aria-label="Sketch of a slitting machine"></div><h4>Slitting</h4><p>Lorem ipsum dolor sit amet, consectetur adipiscing elit, sed do eiusmod tempor incididunt.</p><span class="more">VIEW MORE</span></div>
    <div class="card"><div class="art" role="img" aria-label="Sketch of a die cutting press"></div><h4>Die Cutting</h4><p>Lorem ipsum dolor sit amet, consectetur adipiscing elit, sed do eiusmod tempor incididunt.</p><span class="more">VIEW MORE</span></div>
    <div class="card"><div class="art" role="img" aria-label="Sketch of a vacuum forming machine"></div><h4>Vacuum forming</h4><p>Lorem ipsum dolor sit amet, consectetur adipiscing elit, sed do eiusmod tempor incididunt.</p><span class="more">VIEW MORE</span></div>
    <div class="form"><h4>Contact Us Today</h4><div class="field">Name</div><div class="field">Phone</div><div class="field">Email</div><div class="field big">Comments</div><span class="send">SUBMIT</span></div>
  </div>
</div></section>

<section class="products"><div class="wrap">
  <div class="section-title">Our Products <small>(See all)</small></div>
  <div class="pcards">
    <div class="pcard"><div class="art" role="img" aria-label="Photo of a three seam chamber"></div><h4>CORVANE Three Seam Chamber</h4><p>Lorem ipsum dolor sit amet, consectetur adipiscing elit sed do.</p></div>
    <div class="pcard"><div class="art" role="img" aria-label="Photo of ceramic fibre blanket rolls"></div><h4>CORVANE Fiber Blanket</h4><p>Lorem ipsum dolor sit amet, consectetur adipiscing elit sed do.</p></div>
    <div class="pcard"><div class="art" role="img" aria-label="Photo of a combustion chamber kit"></div><h4>CORVANE Combustion Chamber Kit</h4><p>Lorem ipsum dolor sit amet, consectetur adipiscing elit sed do.</p></div>
    <div class="pcard"><div class="art" role="img" aria-label="Photo of a quickset chamber"></div><h4>Corvane Quickset Chamber</h4><p>Lorem ipsum dolor sit amet, consectetur adipiscing elit sed do.</p></div>
  </div>
</div></section>

<div class="band">If you would like to be a distributor of our VELTRA products, please <u>download the credit application</u> and return to us.</div>

<footer class="footer"><div class="wrap">
  <div class="cols">
    <div><h5>CAPABILITIES</h5><ul><li>Casting</li><li>Vacuum Forming</li><li>Slitting</li><li>Laminating</li><li>Waterjet Cutting</li><li>CNC Machining</li><li>Die Cutting</li></ul></div>
    <div><h5>SERVICES</h5><ul><li>Design</li><li>Rapid Prototyping</li><li>Sourcing</li><li>Mixing</li><li>Assembly</li></ul></div>
    <div><h5>MARKETS</h5><ul><li>Appliances</li><li>Glass</li><li>Wood Stove</li><li>Manufactured</li></ul></div>
    <div><h5>MATERIALS</h5><ul><li>Polycrystalline</li><li>Microporous</li><li>Ceramic Fiber</li><li>Bio-soluble Wool</li><li>Mineral Wool</li><li>Fiber Glass</li></ul></div>
    <div><h5>DOCUMENTATION</h5><ul><li>SDS Sheets</li><li>MSDS Sheets</li><li>T &amp; C</li></ul></div>
    <div><h5>CONTACT US</h5><ul><li>RFQ</li><li>Contact Us</li><li>About Us</li></ul></div>
  </div>
  <div class="fmeta">
    <div class="item"><svg width="12" height="16"><path d="M6 0a6 6 0 0 1 6 6c0 4-6 10-6 10S0 10 0 6a6 6 0 0 1 6-6z" fill="#c7d3e0"/></svg><div>Corvane Manufacturing<br>120 Foundry Lane<br>Millbrook, MA 01900<br>Tel: 555.014.2200<br>Fax: 555.014.2201<br>Hours: Mon-Fri<br>8:00am to 4:30pm</div></div>
    <div class="item"><svg width="14" height="10"><rect width="14" height="10" fill="#c7d3e0"/></svg><div>Sales<br>sales@corvanemfg.com<br><br>Orders<br>orders@corvanemfg.com<br><br>Technical Support<br>tech@corvanemfg.com</div></div>
    <div class="map" role="img" aria-label="Street map showing the company location"></div>
  </div>
</div></footer>
<div class="bottom"><div class="wrap"><span>&copy; 2015 Corvane Manufacturing. All rights reserved.</span><span>Design by Studio</span></div></div>
</body>
</html>
```